KQM Advisory Corporate Brochure

KQM Advisory is a management consulting firm.

We need a corporate brochure showcasing our methodologies (two process diagrams) and our leadership team.

We would like it to look corporate, professional, clean and contemporary.

Happy to have duo tones using our KQM logo colours or mono pics.

Also like texture and 3 dimensional backgrounds and graphics.

We are waiting for head and shoulder photos of a couple of our Associate Directors (can you use placeholders while we obtain these please?)

Our web site is:

www.kqmadvisory-example.com.au

Thanks for your ideas.

Industry/Entity Type

Management Consulting

```html
<!DOCTYPE html>
<html lang="en">
<head>
<meta charset="utf-8">
<title>KQM Advisory Corporate Brochure</title>
<link href="https://fonts.googleapis.com/css2?family=Open+Sans:ital,wght@0,400;0,600;0,700;1,400&display=swap" rel="stylesheet">
<style>
:root{
  --teal:#1d7084;
  --teal-dark:#135868;
  --teal-light:#2a8fa3;
  --box:#1f6f7c;
  --grey-box:#8b8e91;
  --arrow:#2b6f96;
  --text:#3a3a3a;
  --paper:#ffffff;
  --paper-shade:#eeeeee;
  --bg:#e7e5e1;
}
*{box-sizing:border-box;margin:0;padding:0}
html,body{width:1200px;height:900px;overflow:hidden}
body{background:var(--bg);font-family:"Open Sans",Arial,sans-serif;color:var(--text)}
.sheet-grid{display:grid;grid-template-columns:600px 600px;grid-template-rows:450px 450px;width:1200px;height:900px}
.quadrant{display:flex;align-items:center;justify-content:center;border-right:1px solid #d6d3ce;border-bottom:1px solid #d6d3ce}
.spread{display:flex;width:570px;height:400px;box-shadow:0 3px 10px rgba(0,0,0,.18)}
.page{position:relative;width:285px;height:400px;background:var(--paper);overflow:hidden;padding:14px 14px 0}
.page--left{background:linear-gradient(90deg,#fff 85%,var(--paper-shade))}
.page--right{background:linear-gradient(90deg,var(--paper-shade),#fff 15%)}
.wave{position:absolute;left:0;bottom:0;width:285px;height:62px}
.page-url{position:absolute;right:12px;bottom:6px;font-size:5.5px;color:#fff;letter-spacing:.2px}
p,li{font-size:5.4px;line-height:1.5}
p+p{margin-top:5px}
/* cover */
.cover-back{background:linear-gradient(160deg,var(--teal-light),var(--teal) 45%,var(--teal-dark));color:#fff;padding:0}
.follow{position:absolute;left:92px;top:110px;font-size:9px;font-weight:600}
.follow-badge{position:absolute;left:118px;top:128px;display:flex;align-items:center;gap:4px;font-size:8px;font-weight:700}
.follow-badge span.square{width:16px;height:16px;background:#fff;display:block;border-radius:2px}
.brand{display:flex;align-items:center;gap:5px;font-weight:700}
.brand .dot{width:14px;height:14px;border-radius:50%;display:block}
.cover-back .brand{position:absolute;left:14px;top:318px;font-size:11px;color:#fff}
.cover-back .brand .dot{background:#fff}
.tagline{position:absolute;left:14px;top:338px;font-size:4.5px;opacity:.9}
.contact{position:absolute;left:86px;top:352px;display:flex;gap:12px;font-size:4.5px;line-height:1.5}
.contact-item{display:flex;gap:3px;align-items:flex-start}
.cover-url{position:absolute;left:150px;top:382px;font-size:6px;opacity:.9}
.cover-front{padding:0}
.cover-front .brand{position:absolute;left:118px;top:22px;font-size:11px;color:var(--teal)}
.cover-front .brand .dot{background:var(--teal)}
.cover-art{position:absolute;left:10px;top:58px;width:265px;height:270px;background:radial-gradient(circle at 55% 40%,#f6e9a8,#a9d8d8 55%,#e7a14a)}
/* intro */
h2.intro-title{font-size:9px;color:var(--teal);font-weight:700;margin-bottom:3px}
.intro-list{margin:3px 0 4px 8px}
.value-chain{display:block;margin:2px 0 6px}
.quote{font-style:italic;color:var(--teal)}
.vision em{color:var(--teal)}
h3.drivers-title{font-size:7.5px;color:var(--teal);text-align:center;margin:8px 0 4px;font-weight:700}
.drivers-list{margin:4px 0 4px 8px}
/* profiles */
.profile{display:flex;gap:8px}
.photo-slot{flex:0 0 62px;height:80px;background:var(--grey-box);color:#fff;font-size:5px;display:flex;align-items:center;justify-content:center}
.photo{flex:0 0 70px;height:88px;background:linear-gradient(160deg,#d9d9d9,#8a8a8a)}
.profile-name{font-size:7px;color:var(--teal);font-weight:700;margin-bottom:2px}
.profile-body{margin-top:6px}
</style>
</head>
<body>
<main class="sheet-grid">

  <section class="quadrant">
    <div class="spread">
      <div class="page cover-back">
        <div class="follow">Follow us on:</div>
        <div class="follow-badge"><span class="square"></span>NetLink</div>
        <div class="brand"><span class="dot"></span>KQM Advisory</div>
        <div class="tagline">Insight | Method | Results</div>
        <div class="contact">
          <div class="contact-item">
            <svg width="6" height="8" viewBox="0 0 6 8"><path d="M3 0a3 3 0 0 1 3 3c0 2-3 5-3 5S0 5 0 3a3 3 0 0 1 3-3z" fill="#fff"/></svg>
            <span>L9 Harbour House, 40 Example St<br>Perth WA 6000</span>
          </div>
          <div class="contact-item">
            <svg width="7" height="7" viewBox="0 0 7 7"><path d="M1 0h2l1 2-1 1a4 4 0 0 0 1 1l1-1 2 1v2a1 1 0 0 1-1 1C3 7 0 4 0 1a1 1 0 0 1 1-1z" fill="#fff"/></svg>
            <span>+61 8 9000 0000<br>info@kqmadvisory-example.com.au</span>
          </div>
        </div>
        <div class="cover-url">www.kqmadvisory-example.com.au</div>
      </div>
      <div class="page cover-front">
        <div class="brand"><span class="dot"></span>KQM Advisory</div>
        <div class="cover-art" role="img" aria-label="Colourful illustration of the word Growth with figures, gears, rising arrows and city buildings"></div>
        <svg class="wave" viewBox="0 0 285 62" preserveAspectRatio="none"><path d="M0 30 C80 10 170 50 285 20 V62 H0Z" fill="var(--teal)"/><path d="M0 26 C80 6 170 46 285 16" stroke="#b9b9b9" stroke-width="2" fill="none"/></svg>
      </div>
    </div>
  </section>

  <section class="quadrant">
    <div class="spread">
      <div class="page page--left">
        <h2 class="intro-title">Introduction</h2>
        <p>KQM Advisory offers a suite of highly effective and useable Business Process Improvement, Business Strategy and Project Management services.<br>With over 30 years experience of developing more effective business processes and strategy for our clients through our CORE program, KQM achieves dramatic improvements for clients across all value drivers by focusing on four key enablers.</p>
        <ul class="intro-list">
          <li>Systems that enable consistent execution of strategy;</li>
          <li>Processes that are optimised for customers and staff;</li>
          <li>Employees that are empowered and engaged; and</li>
          <li>Channel strategies that engage and meet the needs of customers.</li>
        </ul>
        <svg class="value-chain" width="257" height="120" viewBox="0 0 257 120" font-family="Open Sans, sans-serif" font-size="4.2" fill="#fff" text-anchor="middle">
          <polygon points="0,2 150,2 158,11 150,20 0,20" fill="var(--arrow)"/>
          <text x="18" y="13">System</text><text x="55" y="9">Processes</text><text x="55" y="15">&amp; Practices</text>
          <text x="95" y="9">Empowered</text><text x="95" y="15">Employees</text><text x="132" y="9">Customers</text><text x="132" y="15">&amp; Channels</text>
          <rect x="0" y="52" width="24" height="26" fill="var(--box)"/><text x="12" y="63">Existing</text><text x="12" y="69">Processes</text>
          <rect x="30" y="40" width="28" height="40" fill="var(--box)"/><text x="44" y="56">Optimisation</text><text x="44" y="62">of Systems</text><text x="44" y="68">&amp; Technology</text>
          <rect x="62" y="40" width="28" height="40" fill="var(--box)"/><text x="76" y="56">Delivering</text><text x="76" y="62">Better</text><text x="76" y="68">Practice</text>
          <rect x="94" y="26" width="28" height="16" fill="var(--box)"/><text x="108" y="33">People</text><text x="108" y="39">Culture</text>
          <rect x="94" y="46" width="28" height="16" fill="var(--box)"/><text x="108" y="53">Effective</text><text x="108" y="59">Training</text>
          <rect x="94" y="66" width="28" height="16" fill="var(--box)"/><text x="108" y="73">Org</text><text x="108" y="79">Structure</text>
          <rect x="126" y="26" width="26" height="16" fill="var(--box)"/><text x="139" y="33">Customers</text><text x="139" y="39">Markets</text>
          <rect x="126" y="46" width="26" height="16" fill="var(--box)"/><text x="139" y="53">Products</text><text x="139" y="59">Services</text>
          <rect x="126" y="66" width="26" height="16" fill="var(--box)"/><text x="139" y="73">Delivery</text><text x="139" y="79">Channels</text>
          <rect x="156" y="40" width="30" height="40" fill="var(--box)"/><text x="171" y="56">Desired</text><text x="171" y="62">Future State</text><text x="171" y="68">Organisation</text>
          <rect x="30" y="88" width="28" height="16" fill="var(--grey-box)"/><text x="44" y="98">Systems</text>
          <rect x="62" y="88" width="28" height="16" fill="var(--grey-box)"/><text x="76" y="98">Processes</text>
          <rect x="94" y="88" width="28" height="16" fill="var(--grey-box)"/><text x="108" y="98">Employees</text>
          <rect x="126" y="88" width="26" height="16" fill="var(--grey-box)"/><text x="139" y="98">Customers</text>
          <rect x="30" y="108" width="60" height="10" fill="var(--box)"/><text x="60" y="115">Enabling Levers</text>
          <rect x="94" y="108" width="28" height="10" fill="var(--box)"/><text x="108" y="115">People Levers</text>
          <rect x="126" y="108" width="26" height="10" fill="var(--box)"/><text x="139" y="115">Strategic</text>
        </svg>
        <p>At the same time, KQM programs deliver an empowered and engaged workforce and all of the benefits that arise from such positive outcomes.</p>
        <p class="quote">"Delivering efficiency gains as high as 20% may seem far-fetched, but that is what we have achieved... again and again"</p>
        <svg class="wave" viewBox="0 0 285 62" preserveAspectRatio="none"><path d="M0 40 C90 30 190 58 285 44 V62 H0Z" fill="var(--teal)"/><path d="M0 36 C90 26 190 54 285 40" stroke="#b9b9b9" stroke-width="1.5" fill="none"/></svg>
      </div>
      <div class="page page--right">
        <p class="vision">The KQM vision is to <em>build a Community of Experts that deliver on their promises, by respectful and sustained partnering with clients.</em> To support this we constantly research, develop and apply innovative and sustainable programs that enable our clients to be successful, by improving and optimising the value drivers of their organisation.</p>
        <h3 class="drivers-title">The KQM Advisory optimised value Drivers</h3>
        <svg width="257" height="112" viewBox="0 0 257 112" font-family="Open Sans, sans-serif" font-size="4" fill="#fff" text-anchor="middle">
          <g stroke="#999" stroke-width=".8">
            <line x1="45" y1="20" x2="108" y2="50"/><line x1="128" y1="24" x2="128" y2="44"/><line x1="212" y1="20" x2="148" y2="50"/>
            <line x1="60" y1="56" x2="100" y2="56"/><line x1="196" y1="56" x2="156" y2="56"/>
            <line x1="45" y1="92" x2="108" y2="64"/><line x1="128" y1="88" x2="128" y2="68"/><line x1="212" y1="92" x2="148" y2="64"/>
          </g>
          <rect x="8" y="2" width="70" height="22" fill="var(--box)"/><text x="43" y="11">Processes are designed</text><text x="43" y="17">for stakeholder needs</text>
          <rect x="93" y="2" width="70" height="22" fill="var(--box)"/><text x="128" y="11">Systems and tools to</text><text x="128" y="17">deliver effectively</text>
          <rect x="178" y="2" width="70" height="22" fill="var(--box)"/><text x="213" y="11">The right organisation</text><text x="213" y="17">structure for outcomes</text>
          <rect x="0" y="44" width="60" height="24" fill="var(--box)"/><text x="30" y="54">People with skills</text><text x="30" y="60">and knowledge</text>
          <rect x="100" y="44" width="56" height="24" fill="var(--grey-box)"/><text x="128" y="54">KQM Advisory</text><text x="128" y="60">Optimised Drivers</text>
          <rect x="196" y="44" width="61" height="24" fill="var(--box)"/><text x="226" y="54">Measurement and</text><text x="226" y="60">feedback processes</text>
          <rect x="8" y="88" width="70" height="22" fill="var(--box)"/><text x="43" y="97">Corporate culture and</text><text x="43" y="103">leadership drive</text>
          <rect x="93" y="88" width="70" height="22" fill="var(--box)"/><text x="128" y="97">Operations managed</text><text x="128" y="103">to deliver outcomes</text>
          <rect x="178" y="88" width="70" height="22" fill="var(--box)"/><text x="213" y="97">The right controls</text><text x="213" y="103">to minimise risks</text>
        </svg>
        <ul class="drivers-list">
          <li>Preparing for a merger or acquisition</li>
          <li>Seeking accelerated growth</li>
          <li>Requiring 'turnaround'</li>
          <li>Undergoing a restructure</li>
          <li>Introducing new products or services</li>
          <li>Entering new markets</li>
          <li>Preparing for an IPO or management buyout</li>
          <li>Facing unique challenges</li>
        </ul>
        <p>Our clients include some of Australia's most respected businesses and government agencies across Australia.</p>
        <p>KQM services are used by private sector clients:</p>
        <svg class="wave" viewBox="0 0 285 62" preserveAspectRatio="none"><path d="M0 44 C90 58 190 30 285 40 V62 H0Z" fill="var(--teal)"/><path d="M0 40 C90 54 190 26 285 36" stroke="#b9b9b9" stroke-width="1.5" fill="none"/></svg>
        <span class="page-url">www.kqmadvisory-example.com.au</span>
      </div>
    </div>
  </section>

  <section class="quadrant">
    <div class="spread">
      <div class="page page--left">
        <div class="profile">
          <div class="photo-slot">Picture to come</div>
          <div>
            <h4 class="profile-name">Daniel Marsh – Associate Director</h4>
            <p>Daniel has over eighteen (18) years experience of management and business consultancy services to the Oil &amp; Gas, Resources, Financial and Government sectors.</p>
            <p>He has successfully delivered projects that have required expertise in the areas of Management Information Systems Design and Implementation, Business Process Re-engineering and Procedure Development, Project Performance Monitoring, Portfolio Management and Performance Benchmarking.</p>
          </div>
        </div>
        <div class="profile-body">
          <p>Daniel's key strength is in Project Management where he has a wealth of experience in the development and implementation of best practise project controls policies, standards, guidelines and procedures (including contract, cost, schedule, estimating, forecasting, benchmarking and portfolio Management).</p>
          <p>Daniel not only provides the technical skills and know how to deliver successful project outcomes but he does this in a way that brings the human element into project management, enabling organisations, teams and individuals to achieve their full potential.</p>
          <p>Daniel has developed a series of workshops to assist with cultural alignment within organisations to achieve project success. The workshops are run with the project team and other stakeholders at the project initiation stage.</p>
          <p>Project Success Workshops cover a number of key areas including project strategy definition and organisational readiness reviews, project team alignment, project roadmap development, EPC(M) alignment project execution and tollgating.</p>
          <p>Daniel is also Founder / Managing Director of NextStep, a specialist consultancy enabling organisations, teams and individuals to achieve their true potential.</p>
          <p>He is passionate about 'giving back' and in 2011 founded the Coast to Cape Men's Health Ride to raise awareness levels of prostate cancer and funds for prostate cancer research.</p>
        </div>
        <svg class="wave" viewBox="0 0 285 62" preserveAspectRatio="none"><path d="M0 40 C90 30 190 58 285 44 V62 H0Z" fill="var(--teal)"/><path d="M0 36 C90 26 190 54 285 40" stroke="#b9b9b9" stroke-width="1.5" fill="none"/></svg>
      </div>
      <div class="page page--right">
        <svg class="wave" viewBox="0 0 285 62" preserveAspectRatio="none"><path d="M0 44 C90 58 190 30 285 40 V62 H0Z" fill="var(--teal)"/><path d="M0 40 C90 54 190 26 285 36" stroke="#b9b9b9" stroke-width="1.5" fill="none"/></svg>
        <span class="page-url">www.kqmadvisory-example.com.au</span>
      </div>
    </div>
  </section>

  <section class="quadrant">
    <div class="spread">
      <div class="page page--left">
        <div class="profile">
          <div class="photo" role="img" aria-label="Black and white head and shoulders portrait of the Director"></div>
          <div>
            <h4 class="profile-name">Paul Harding – Director</h4>
            <p>Paul is a business strategist and project manager with more than 25 years of experience at an international level across different business categories in the public and private sector with a focus on achieving successful commercial outcomes.</p>
            <p>Paul has been involved in shaping the success of a number organisations, the largest of which is Tide Digital a Australian telecommunications service provider backed by Alan Rourke that went on to become publicly listed with an annual turnover in excess of half a billion dollars.</p>
          </div>
        </div>
        <div class="profile-body">
          <p>Paul has experience across a number of different businesses categories with particular expertise and experience gained at Tide Digital in the application of channel strategies to sales, distribution and customer management.</p>
          <p>He has been involved in the procurement and delivery of several major projects in Australia, the most recent of which required him to oversee the tender and delivery of a residential construction project in regional Western Australia.</p>
          <p>Successfully implementing this high profile and complex project required Paul to manage many project stakeholders including lawyers, accountants, property valuers, developers, local councils, government agencies and a private sector partners.</p>
          <p>Other notable project involvement has been the merger of two major financial institutions, the international roll out of new software for Harbourside Petroleum, the national refurbishment program of Grocer Co supermarkets and a review of all online activity for the Department of Education and Training.</p>
          <p>In 2010 Paul established an initiative to encourage large businesses in Australia to reduce their carbon emissions caused by the use of paper-based communications. In it's first year this initiative funded the planting of 7000 native trees in New South Wales to sequester carbon.</p>
          <p>Paul has delivered strategic projects with successful outcomes for organisations in London, Singapore and Australia.</p>
        </div>
        <svg class="wave" viewBox="0 0 285 62" preserveAspectRatio="none"><path d="M0 40 C90 30 190 58 285 44 V62 H0Z" fill="var(--teal)"/><path d="M0 36 C90 26 190 54 285 40" stroke="#b9b9b9" stroke-width="1.5" fill="none"/></svg>
      </div>
      <div class="page page--right">
        <div class="profile">
          <div class="photo-slot">Picture</div>
          <div>
            <h4 class="profile-name">Mark Ellison – Associate Director</h4>
            <p>Mark is a senior business leader with 30 years experience with Coastline Energy International and Meridian Power developing and leading business in the Energy sector.</p>
            <p>During his career at Coastline Energy International Mark advised business units around the world on business development and had postings to Germany, China and Russia. These assignments required Mark to lead teams in the development and improvement of the business in diverse cultures and acquire a good understanding of the structure and processes of a multinational company.</p>
          </div>
        </div>
        <div class="profile-body">
          <p>At Meridian Power Mark was a senior member of the Executive and interfaced regularly with the Board to discuss business performance and strategy. In addition he engaged frequently with senior stakeholders from both the private and public sectors.</p>
          <p>Mark operates effectively at the highest levels within organisations and has a good understanding of the functions, interdependencies and processes of the Departments of Treasury, Premier and Cabinet, Public Utilities, State Development and The Regional Development Commissions.</p>
          <p>With the combination of international oil company experience together with a network and knowledge of the local Energy/ Resources and Government landscape, Mark has the skills and knowledge to advise clients on a broad range of issues associated with Commercial Business Development, Performance Improvement, Infrastructure Planning and Strategy.</p>
        </div>
        <svg class="wave" viewBox="0 0 285 62" preserveAspectRatio="none"><path d="M0 44 C90 58 190 30 285 40 V62 H0Z" fill="var(--teal)"/><path d="M0 40 C90 54 190 26 285 36" stroke="#b9b9b9" stroke-width="1.5" fill="none"/></svg>
        <span class="page-url">www.kqmadvisory-example.com.au</span>
      </div>
    </div>
  </section>

</main>
</body>
</html>
```